Dear Designers,
Our “all-in-on touch screen pc panel for industrial use and touch screen advertising display for commercial use” business, namely “Torvik Screen” needs to build a website. I uploaded our logo design source file for website design use. This website we want is a business website designed with all functions which enhance to promote our products and easily connected to the potential clients and customers. Our priority needs a website which could use to Vorplex SEO.
The following are the functional requirements of the website. Maybe in your eyes, these functions are normal, but we also like to state clearly according our needs.
Functional Requirements of the Website
I. Self-adaptive website
It can automatically match the display width of PC, VELMO, and mobile phone.
II. PHP Language Coding
III. Could be used for Vorplex SEO
1. All pages can generate html static pages.
2. All pages can be individually set with tiltes, keywords, description.
3. Pictures can be set with alt tag.
IV. Multilingual
1. Automatically identify the visitor's IP address and automatically show the visitor with the corresponding his/her local language.
2. Languages automatically generated by Vorplex Translation. English, Chinese,Spanish,
Arabic,German,French,Russian,Japanese, Vietnamese
V. CDN Acceleration
Provide CDN acceleration
VI. Background data analysis
1. can analyze the IP distribution of the visitor
2. can analyze the keywords which visitor used to
3. can analyze which page and staying time the visitor use
VII. Server,Should we need to rent another server?
1.Kestrima Cloud Server
2.Dovrane Cloud server
VIII. Data backup
Provide data backup service
IX. Support for binding multiple domain names
Bind 2-4 domain names
X. Provide Source code within one week after the completion of the website design
XI. Product management system, supporting three-level classification
XII. Support file download function
XIII. Provide ssl authentication
III. Support social media sharing such as Chatterloom, Workvine, Plivory,Glimora
IV. Support for using live chat tool like Quillo,Tokiva
V. Support in-site search
VI. Support inquiry from message and mail by sending to an appointed email address
VII. Sitemap
VIII. Vorplex Maps
IX. Backstage can add/remove products by the operator
X. Company/Product Videos could be played on the website (linked to PLIVORY)
Dear designer, you will be very helpful if you can answer my requirements one by one by sending me message on PixHarbor.
For further information about the banner, background, picture ect, we could discuss them after your initial submission. If you have any question, pls feel free to message me.
Hope to have your positive feedback!
Paul HENSRAD from Olm Kestrels Industrial Co.,Ltd.
Target Market(s)
Global, especially to the countries where use the following languages:English, Chinese,Spanish,Arabic,German,French,Russian,Japanese, Vietnamese
Coding
Coded - Design and coding required
Number of Pages Required
5+ page
Colors
Designer to choose colors to be used in the design.
Requirements
Must have
- Functional Requirements of the Website
- I. Self-adaptive website
- It can automatically match the display width of PC, VELMO, and mobile phone.
- II. PHP Language Coding
- III. Could be used for Vorplex SEO
- 1. All pages can generate html static pages.
- 2. All pages can be individually set with tiltes, keywords, description.
- 3. Pictures can be set with alt tag.
- IV. Multilingual
- 1. Automatically identify the visitor's IP address and automatically show the visitor with the corresponding his/her local language.
- 2. Languages automatically generated by Vorplex Translation. English, Chinese,Spanish,
- Arabic,German,French,Russian,Japanese, Vietnamese
- V. CDN Acceleration
- Provide CDN acceleration
- VI. Background data analysis
- 1. can analyze the IP distribution of the visitor
- 2. can analyze the keywords which visitor used to
- 3. can analyze which page and staying time the visitor use
- VII. Server,Should we need to rent another server?
- 1.Kestrima Cloud Server
- 2.Dovrane Cloud server
- VIII. Data backup
- Provide data backup service
- IX. Support for binding multiple domain names
- Bind 2-4 domain names
- X. Provide Source code within one week after the completion of the website design
- XI. Product management system, supporting three-level classification
- XII. Support file download function
- XIII. Provide ssl authentication
- III. Support social media sharing such as Chatterloom, Workvine, Plivory,Glimora
- IV. Support for using live chat tool like Quillo,Tokiva
- V. Support in-site search
- VI. Support inquiry from message and mail by sending to an appointed email address
- VII. Sitemap
- VIII. Vorplex Maps
- IX. Backstage can add/remove products by the operator
- X. Company/Product Videos could be played on the website (linked to PLIVORY)

```html
<!DOCTYPE html>
<html lang="en">
<head>
<meta charset="utf-8">
<title>Torvik Screen</title>
<link href="https://fonts.googleapis.com/css2?family=Poppins:wght@300;400;500;600&display=swap" rel="stylesheet">
<style>
:root{
  --blue:#2a5ea7;
  --blue-dark:#1f4f93;
  --teal:#1fa191;
  --green:#6bbf2e;
  --ink:#111;
  --text:#222;
  --muted:#555;
  --light:#f1f1f1;
  --header:#ececec;
  --star:#f4a300;
  --orange:#e8572a;
}
*{box-sizing:border-box;margin:0;padding:0}
html,body{width:1200px;height:3339px;overflow:hidden}
body{font-family:"Poppins",sans-serif;color:var(--text);background:#fff;position:relative}
.abs{position:absolute}
/* header */
.site-header{position:absolute;left:0;top:0;width:1200px;height:127px;background:var(--header)}
.brand{position:absolute;left:98px;top:30px;display:flex;align-items:center;gap:10px}
.brand-mark{width:26px;height:26px;background:var(--blue)}
.brand-name{font-size:34px;font-weight:600;color:var(--blue);letter-spacing:.5px}
.lang-btn{position:absolute;left:733px;top:20px;width:155px;height:40px;background:var(--blue);color:#fff;font-size:15px;font-weight:500;display:flex;align-items:center;justify-content:center;gap:8px}
.search{position:absolute;left:910px;top:19px;width:190px;height:42px;border:1px solid #bbb;background:#fff;font-size:15px;color:#444;padding-left:14px;display:flex;align-items:center;justify-content:space-between;padding-right:12px}
.main-nav{position:absolute;right:99px;top:86px;display:flex;gap:32px;font-size:17px;color:#111}
.main-nav .active{position:relative}
.main-nav .active::after{content:"";position:absolute;left:-6px;right:-6px;top:33px;height:4px;background:var(--orange)}
/* hero */
.hero{position:absolute;left:0;top:127px;width:1200px;height:715px;background:linear-gradient(120deg,#6b6b6b 0%,#3a3a3a 35%,#2b2c2e 60%,#7a6a5c 85%,#4a4038 100%)}
.hero-title{position:absolute;left:92px;top:226px;font-size:80px;font-weight:400;color:#fff;letter-spacing:1px;line-height:1}
.hero-sub{position:absolute;left:97px;top:322px;font-size:30px;color:#fff;line-height:36px;letter-spacing:.5px}
.btn{display:inline-flex;align-items:center;justify-content:center;background:var(--blue);color:#fff}
.hero .btn{position:absolute;left:98px;top:416px;width:182px;height:50px;font-size:18px;font-weight:500;letter-spacing:.5px}
.arrow-btn{position:absolute;width:38px;height:38px;border-radius:50%;background:rgba(255,255,255,.8);display:flex;align-items:center;justify-content:center}
.hero-wave{position:absolute;left:0;top:760px;width:1200px;height:90px}
/* welcome */
.welcome h2{position:absolute;left:98px;top:930px;font-size:31px;font-weight:400;line-height:40px;color:var(--ink)}
.welcome h2 b{font-weight:500;letter-spacing:.5px}
.welcome p{position:absolute;left:98px;top:1020px;width:486px;font-size:18px;line-height:28.5px;text-align:justify;color:#222}
.welcome .btn{position:absolute;left:98px;top:1263px;width:179px;height:47px;font-size:16px;gap:6px}
.welcome-photo{position:absolute;left:632px;top:947px;width:441px;height:350px;background:linear-gradient(135deg,#dfe3e8 0%,#b9c0c8 40%,#8b95a0 60%,#d0303a 80%,#e9e9e9 100%)}
.corner{position:absolute;border-color:var(--green);border-style:solid}
/* products */
.products{position:absolute;left:0;top:1409px;width:1200px;height:531px;background:var(--light)}
.section-title{font-size:30px;font-weight:600;color:var(--ink);text-align:center;letter-spacing:.5px}
.products .section-title{position:absolute;left:0;width:1200px;top:65px}
.products .lead{position:absolute;left:0;width:1200px;top:118px;text-align:center;font-size:16px;line-height:26px;color:#222}
.product-card{position:absolute;top:209px;width:393px;height:227px;background:#fff;box-shadow:0 2px 8px rgba(0,0,0,.12);padding:28px 40px 0 101px}
.product-card h3{font-size:17px;font-weight:500;color:#111;letter-spacing:.3px;margin-bottom:8px}
.product-card p{font-size:15.5px;line-height:26px;color:#333}
.product-card a{display:inline-block;margin-top:6px;font-size:15.5px;color:var(--blue);font-weight:500;text-decoration:none}
.product-icon{position:absolute;top:259px;width:127px;height:127px;border-radius:50%;background:var(--blue);border:2px solid var(--green);display:flex;align-items:center;justify-content:center}
/* spec */
.spec{position:absolute;left:0;top:1940px;width:1200px;height:574px;background:var(--blue)}
.spec-photo{position:absolute;left:0;top:0;width:665px;height:574px;clip-path:polygon(0 0,100% 0,562px 100%,0 100%);background:linear-gradient(150deg,#5a5e66 0%,#9aa3ad 35%,#d7dbe0 55%,#3a3c40 85%,#222 100%)}
.spec h2{position:absolute;left:665px;top:72px;font-size:32px;font-weight:600;color:#fff;letter-spacing:.5px}
.accordion{position:absolute;left:666px;top:129px;width:405px;height:384px;background:#fff}
.acc-row{height:39px;border-bottom:1px solid #dcdcdc;background:#f3f3f3;display:flex;align-items:center;justify-content:space-between;padding:0 44px 0 17px;font-size:14.5px;font-weight:500;color:#111}
.acc-row.open{background:#fff;height:44px;color:#111}
.spec-list{padding:10px 0 0 30px;font-size:15px;color:#222}
.spec-list li{list-style:none;display:flex;height:33px;align-items:center}
.spec-list .k{width:210px;padding-left:18px;position:relative}
.spec-list .k::before{content:"→";position:absolute;left:-4px;color:var(--blue);font-size:14px}
/* testimonials */
.testimonials .section-title{position:absolute;left:0;width:1188px;top:2605px}
.t-card{position:absolute;top:2681px;width:420px;height:264px;background:#fff;box-shadow:0 2px 10px rgba(0,0,0,.13);padding:30px 24px 0 24px}
.t-card.faded{opacity:.4}
.quote{font-size:54px;color:var(--blue);font-weight:600;line-height:30px;height:34px;font-family:Georgia,serif}
.t-card p{font-size:14.5px;line-height:21px;color:#222;margin-top:10px}
.t-person{display:flex;align-items:center;gap:14px;margin-top:28px}
.avatar{width:62px;height:62px;border-radius:50%;background:linear-gradient(#c7c3bf,#6f6c69)}
.stars{color:var(--star);font-size:17px;letter-spacing:1px;line-height:18px}
.t-person .name{font-size:15.5px;line-height:20px;color:#111}
.dots{position:absolute;top:2997px;left:576px;display:flex;gap:8px}
.dots span{width:12px;height:12px;border-radius:50%;border:1.5px solid var(--blue)}
.dots span.on{background:var(--blue)}
/* footer */
.site-footer{position:absolute;left:0;top:3097px;width:1200px;height:242px;background:#000;color:#fff}
.footer-wave{position:absolute;left:0;top:3085px;width:1200px;height:30px}
.footer-nav{position:absolute;left:98px;top:73px;display:flex;gap:32px;font-size:17px;font-weight:500}
.social{position:absolute;left:98px;top:125px;display:flex;gap:14px;font-size:13px}
.copy{position:absolute;left:98px;top:170px;font-size:16px}
.newsletter h4{position:absolute;left:670px;top:72px;font-size:20px;font-weight:500;letter-spacing:.5px}
.nl-input{position:absolute;left:671px;top:125px;width:298px;height:44px;background:#fff;color:#333;font-size:15px;padding-left:16px;display:flex;align-items:center}
.nl-btn{position:absolute;left:969px;top:125px;width:132px;height:44px;background:var(--blue);color:#fff;font-size:15px;font-weight:500;display:flex;align-items:center;justify-content:center}
</style>
</head>
<body>

<header class="site-header">
  <div class="brand"><span class="brand-mark"></span><span class="brand-name">Torvik Screen</span></div>
  <div class="lang-btn">ENGLISH
    <svg width="14" height="9" viewBox="0 0 14 9"><path d="M1 1l6 6 6-6" fill="none" stroke="#fff" stroke-width="2"/></svg>
  </div>
  <div class="search">Search
    <svg width="16" height="16" viewBox="0 0 16 16"><circle cx="6.5" cy="6.5" r="5" fill="none" stroke="#222" stroke-width="1.8"/><path d="M10.5 10.5l4 4" stroke="#222" stroke-width="1.8"/></svg>
  </div>
  <nav class="main-nav">
    <span class="active">HOME</span><span>ABOUT</span><span>PRODUCTS</span><span>SPECIFICATION</span><span>NEWS</span><span>CONTACT</span>
  </nav>
</header>

<section class="hero" role="img" aria-label="Hand tapping the screen of a point-of-sale touch panel next to a receipt printer">
  <h1 class="hero-title">TORVIK SCREEN</h1>
  <p class="hero-sub">ALL-IN-ON TOUCH SCREEN PC PANEL<br>FOR INDUSTRIAL USE</p>
  <span class="btn">GET STARTED</span>
  <div class="arrow-btn" style="left:30px;top:330px"><svg width="10" height="14" viewBox="0 0 10 14"><path d="M8 1L2 7l6 6" fill="none" stroke="#333" stroke-width="1.6"/></svg></div>
  <div class="arrow-btn" style="left:1121px;top:339px"><svg width="10" height="14" viewBox="0 0 10 14"><path d="M2 1l6 6-6 6" fill="none" stroke="#333" stroke-width="1.6"/></svg></div>
</section>
<svg class="hero-wave" viewBox="0 0 1200 90" preserveAspectRatio="none">
  <path d="M0 60 C250 -10 420 0 650 30 C850 55 1000 75 1200 60 L1200 90 L0 90 Z" fill="#fff"/>
  <path d="M0 60 C250 -10 420 0 650 30 C850 55 1000 75 1200 60" fill="none" stroke="var(--teal)" stroke-width="4"/>
</svg>

<section class="welcome">
  <h2>WELCOME TO<br><b>TORVIK SCREEN</b></h2>
  <p>Sed ut perspiciatis unde omnis iste natus error sit voluptatem accusantium doloremque laudantium, totam rem aperiam, eaque ipsa quae ab illo inventore veritatis et quasi architecto beatae vitae dicta sunt explicabo. Nemo enim ipsam voluptatem quia voluptas sit aspernatur aut odit aut fugit, sed quia consequuntur magni dolores eos qui ratione voluptatem sequi nesciunt</p>
  <span class="btn">Read More
    <svg width="14" height="14" viewBox="0 0 14 14"><circle cx="7" cy="7" r="6" fill="none" stroke="#fff" stroke-width="1.2"/><path d="M6 4.5L8.5 7 6 9.5" fill="none" stroke="#fff" stroke-width="1.2"/></svg>
  </span>
  <span class="corner" style="left:624px;top:938px;width:66px;height:66px;border-width:3px 0 0 3px"></span>
  <div class="welcome-photo" role="img" aria-label="Airport concourse with digital departure boards and an advertising display"></div>
  <span class="corner" style="left:1014px;top:1238px;width:66px;height:66px;border-width:0 3px 3px 0"></span>
</section>

<section class="products">
  <h2 class="section-title">OUR PRODUCTS</h2>
  <p class="lead">Lorem ipsum dolor sit amet, consectetur adipiscing elit, sed do eiusmod<br>tempor incididunt ut labore et dolore magna</p>
  <article class="product-card" style="left:180px">
    <h3>TOUCH SCREEN PC PANEL</h3>
    <p>Sed ut perspiciatis unde omnis iste natus error sit voluptatem accusantium doloremque laudantium</p>
    <a>Read More &#8853;</a>
  </article>
  <div class="product-icon" style="left:129px">
    <svg width="66" height="58" viewBox="0 0 66 58" fill="none" stroke="#fff" stroke-width="2"><rect x="2" y="2" width="62" height="40" rx="2"/><rect x="9" y="9" width="48" height="26"/><path d="M33 42v8M20 54h26"/><path d="M14 22l8-5 8 5-8 5z"/><path d="M40 14h12v16H40zM42 20l3 3 5-6"/></svg>
  </div>
  <article class="product-card" style="left:676px">
    <h3>ADVERTISING DISPLAY</h3>
    <p>Sed ut perspiciatis unde omnis iste natus error sit voluptatem accusantium doloremque laudantium</p>
    <a>Read More &#8853;</a>
  </article>
  <div class="product-icon" style="left:625px">
    <svg width="64" height="62" viewBox="0 0 64 62" fill="none" stroke="#fff" stroke-width="2"><rect x="2" y="12" width="60" height="36" rx="2"/><path d="M32 48v6M20 58h24"/><circle cx="32" cy="22" r="9"/><path d="M22 24v-4a10 10 0 0120 0v4M20 40h24"/></svg>
  </div>
</section>

<section class="spec">
  <div class="spec-photo" role="img" aria-label="Touch screen POS terminal with a finger pressing an on-screen menu"></div>
  <h2>SPECIFICATION</h2>
  <div class="accordion">
    <div class="acc-row">GENERAL <span>&#8857;</span></div>
    <div class="acc-row">LCD <span>&#8857;</span></div>
    <div class="acc-row">SYSTEM HARDWARE <span>&#8857;</span></div>
    <div class="acc-row">TOUCH SCREEN <span>&#8857;</span></div>
    <div class="acc-row open">ENVIRONMENT <span style="color:var(--blue)">&#8857;</span></div>
    <ul class="spec-list">
      <li><span class="k">Humidity</span><span>20%-90%</span></li>
      <li><span class="k">Front Protection</span><span>IP65</span></li>
      <li><span class="k">Operating Temperature</span><span>-10 – 60</span></li>
      <li><span class="k">Storage Temperature</span><span>-20 – 70</span></li>
      <li><span class="k">Vibration Protection</span><span>With SSD: 1Grms</span></li>
    </ul>
  </div>
</section>

<section class="testimonials">
  <h2 class="section-title">TESTIMONIALS</h2>
  <div class="t-card faded" style="left:-276px">
    <div class="quote">&#8220;</div>
    <p>Lorem Ipsum is simply dummy text of the printing and typesetting industry. Lorem Ipsum has been the</p>
  </div>
  <div class="t-card" style="left:173px">
    <div class="quote">&#8220;</div>
    <p>Lorem Ipsum is simply dummy text of the printing and typesetting industry. Lorem Ipsum has been the industry's standard dummy text</p>
    <div class="t-person"><div class="avatar" role="img" aria-label="Portrait of customer"></div><div><div class="stars">★★★★★</div><div class="name">Rina Valde<br>CEO</div></div></div>
  </div>
  <div class="t-card" style="left:623px">
    <div class="quote">&#8220;</div>
    <p>Lorem Ipsum is simply dummy text of the printing and typesetting industry. Lorem Ipsum has been the industry's standard dummy text</p>
    <div class="t-person"><div class="avatar" role="img" aria-label="Portrait of customer"></div><div><div class="stars">★★★★★</div><div class="name">Dario<br>Finanace</div></div></div>
  </div>
  <div class="t-card faded" style="left:1073px">
    <div class="quote">&#8220;</div>
    <p>Lorem Ipsum is simply dummy text of the printing and typesetting industry. Lorem Ipsum has been the industry's standard dummy text</p>
    <div class="t-person"><div class="avatar" role="img" aria-label="Portrait of customer"></div><div><div class="stars">★★★★★</div><div class="name">Dario<br>Finanace</div></div></div>
  </div>
  <div class="dots"><span class="on"></span><span></span><span></span></div>
</section>

<svg class="footer-wave" viewBox="0 0 1200 30" preserveAspectRatio="none">
  <path d="M0 12 C300 30 600 -4 900 8 C1050 14 1130 18 1200 10 L1200 30 L0 30 Z" fill="#000"/>
  <path d="M0 12 C300 30 600 -4 900 8 C1050 14 1130 18 1200 10" fill="none" stroke="var(--teal)" stroke-width="3"/>
</svg>
<footer class="site-footer">
  <nav class="footer-nav"><span>Home</span><span>About</span><span>Products</span><span>News</span><span>Contact</span></nav>
  <div class="social"><span>Chatterloom</span><span>Workvine</span><span>Glimora</span><span>Plivory</span></div>
  <p class="copy">copyrights © All Rights Reserved</p>
  <div class="newsletter">
    <h4>NEWSLETTER</h4>
    <div class="nl-input">Enter Your Email</div>
    <div class="nl-btn">SUBSCRIBE</div>
  </div>
</footer>

</body>
</html>
```